Business Card Design Project

We would need a business name card for our online website business, http://www.brindle.com.sg/. We would need to include our website on the name card as well.

Target Market(s)

Adults and kids in Singapore, mainly expatriates

Industry/Entity Type

Business

Font styles to use
Sans Serif

Colors

Designer to choose colors to be used in the design.

Requirements
Must have
• Must include our "vorn" logo and we would like our name card to be printed on light craft paper material

```html
<!DOCTYPE html>
<html lang="en">
<head>
<meta charset="utf-8">
<title>vorn business card</title>
<link rel="stylesheet" href="https://fonts.googleapis.com/css2?family=Arimo:wght@400;700&display=swap">
<style>
  :root {
    --backdrop: #1b1b1b;
    --card-light: #f1f0f0;
    --card-shade: #c9c8c9;
    --navy: #26387a;
    --red: #d0232c;
    --ink: #1c1c1c;
    --ink-soft: #2e2e3a;
  }
  html, body {
    margin: 0;
    width: 1200px;
    height: 1134px;
    overflow: hidden;
    background: var(--backdrop);
    font-family: "Arimo", Arial, sans-serif;
  }
  .sheet { display: block; width: 1200px; height: 1134px; }
  .brand-name { font-family: "Arimo", Arial, sans-serif; font-weight: 700; fill: var(--navy); letter-spacing: 4px; }
  .person-name { font-family: "Arimo", Arial, sans-serif; font-size: 46px; fill: var(--ink-soft); }
  .person-name .initial { fill: var(--navy); }
  .contact-line { font-family: "Arimo", Arial, sans-serif; font-size: 22px; fill: var(--ink); letter-spacing: 2px; }
  .web-address { font-family: "Arimo", Arial, sans-serif; font-size: 34px; fill: var(--ink); letter-spacing: 1px; }
  .icon { fill: none; stroke: var(--navy); stroke-width: 2; }
</style>
</head>
<body>
<svg class="sheet" viewBox="0 0 1200 1134" xmlns="http://www.w3.org/2000/svg" aria-label="vorn business card, back and front">
  <defs>
    <linearGradient id="panel-left" x1="0" y1="0" x2="1" y2="1">
      <stop offset="0" stop-color="var(--card-shade)"/>
      <stop offset="0.55" stop-color="var(--card-light)"/>
      <stop offset="1" stop-color="#dcdbdb"/>
    </linearGradient>
    <linearGradient id="panel-right" x1="0" y1="0" x2="1" y2="0">
      <stop offset="0" stop-color="#d8d7d7"/>
      <stop offset="1" stop-color="var(--card-light)"/>
    </linearGradient>
    <radialGradient id="face-glow" cx="0.55" cy="0.45" r="0.7">
      <stop offset="0" stop-color="#f7f7f7"/>
      <stop offset="1" stop-color="#bdbcbd"/>
    </radialGradient>
    <clipPath id="back-clip"><rect x="180" y="70" width="840" height="480"/></clipPath>
    <clipPath id="front-clip"><rect x="180" y="590" width="840" height="480"/></clipPath>
  </defs>

  <!-- Card back: brand panel and contact panel -->
  <g class="card card-back" clip-path="url(#back-clip)">
    <rect x="180" y="70" width="420" height="480" fill="url(#panel-left)"/>
    <rect x="600" y="70" width="420" height="480" fill="url(#panel-right)"/>
    <line x1="600" y1="70" x2="600" y2="550" stroke="#a9a8a9" stroke-width="1.5"/>
    <path class="band-top" d="M180 70 H1020 V104 Q600 136 180 96 Z" fill="var(--navy)"/>
    <path d="M180 96 Q600 136 1020 104" fill="none" stroke="var(--red)" stroke-width="4"/>
    <path class="band-bottom" d="M180 550 H1020 V522 Q600 490 180 512 Z" fill="var(--navy)"/>
    <path d="M180 512 Q600 490 1020 522" fill="none" stroke="var(--red)" stroke-width="4"/>

    <g class="brand-mark">
      <circle cx="310" cy="310" r="26" fill="var(--red)"/>
      <text class="brand-name" x="352" y="328" font-size="50">VORN</text>
    </g>

    <g class="contact-block">
      <text class="person-name" x="640" y="248"><tspan class="initial">Y</tspan>our Name</text>
      <g transform="translate(652 286)">
        <path class="icon" d="M0 -10 a7 7 0 0 1 7 7 c0 6 -7 13 -7 13 c0 0 -7 -7 -7 -13 a7 7 0 0 1 7 -7 z"/>
        <circle class="icon" cx="0" cy="-3" r="2.5"/>
      </g>
      <text class="contact-line" x="676" y="294">Your address</text>
      <rect class="icon" x="646" y="312" width="12" height="20" rx="2"/>
      <text class="contact-line" x="676" y="330">000-000-0000</text>
      <g transform="translate(644 350)">
        <rect class="icon" x="0" y="0" width="18" height="13"/>
        <path class="icon" d="M0 0 L9 7 L18 0"/>
      </g>
      <text class="contact-line" x="676" y="364">Email@</text>
    </g>
  </g>

  <!-- Card front: brand mark and web address -->
  <g class="card card-front" clip-path="url(#front-clip)">
    <rect x="180" y="590" width="840" height="480" fill="url(#face-glow)"/>
    <path class="corner-top" d="M180 590 H440 Q330 700 180 720 Z" fill="var(--navy)"/>
    <path d="M440 590 Q330 700 180 720" fill="none" stroke="var(--red)" stroke-width="4"/>
    <path class="corner-bottom" d="M1020 1070 H770 Q870 960 1020 940 Z" fill="var(--navy)"/>
    <path d="M770 1070 Q870 960 1020 940" fill="none" stroke="var(--red)" stroke-width="4"/>

    <g class="brand-mark">
      <circle cx="478" cy="808" r="36" fill="var(--red)"/>
      <text class="brand-name" x="536" y="834" font-size="72">VORN</text>
    </g>
    <text class="web-address" x="600" y="990" text-anchor="middle">www.brindle.com.sg</text>
  </g>
</svg>
</body>
</html>
```